Business Card - Rebranding for Consulting Firm

We are renaming and rebranding our consulting firm and need to raise the level of quality of our cards as part of that effort. We consult to leading high tech, life science and other innovation sector companies.

Need a two-sided business card design.

Side 1: (a) Company logo (b) tag line: Optimize Your Investment in Talent (c) Name (d) Title (e) Phone 1: Office (f) Phone 2: Mobile (g) email: person@HollowmereAdvisory.com

Side 2: Two lines of text: (a) Growth is Imperative. Change is Constant. Talent Executes Strategy. (b) We help you excel at all three.

Target Market(s)

Business and human resources executives and senior managers

Industry/Entity Type

Management Consulting

Contact Information for Business Card

Font styles to use
Sans Serif

Requirements
Must have
• clean, not too busy, but with a bit of creativity. Stick to the colors used in the attached logo
• appeal to high tech, life science companies
Nice to have
• prefer white background

```html
<!DOCTYPE html>
<html lang="en">
<head>
<meta charset="utf-8">
<title>Hollowmere Advisory – Business Card</title>
<link href="https://fonts.googleapis.com/css2?family=Fira+Sans+Condensed:wght@300;400;500&family=Montserrat:wght@600&display=swap" rel="stylesheet">
<style>
  :root {
    --brand-blue: #066ca6;
    --paper: #ffffff;
    --ink-grey: #8b949b;
    --tag-grey: #6f7c86;
    --backdrop: #e9ebed;
  }
  html, body {
    margin: 0;
    width: 1200px;
    height: 1200px;
    overflow: hidden;
    background: var(--backdrop);
  }
  .canvas {
    position: relative;
    width: 1200px;
    height: 1200px;
  }
  .card {
    position: absolute;
    width: 714px;
    height: 408px;
    box-shadow: 0 6px 18px rgba(0,0,0,0.18);
    overflow: hidden;
  }
  .card-front { left: 240px; top: 174px; background: var(--paper); }
  .card-back  { left: 245px; top: 617px; background: var(--brand-blue); }

  .side-band {
    position: absolute;
    left: 616px;
    top: 0;
    width: 98px;
    height: 408px;
    background: var(--brand-blue);
  }

  .wordmark {
    position: absolute;
    left: 50px;
    top: 56px;
    display: flex;
    align-items: center;
    gap: 14px;
    font-family: "Fira Sans Condensed", sans-serif;
    font-weight: 500;
    font-size: 48px;
    line-height: 1;
    color: var(--brand-blue);
  }
  .wordmark-square {
    width: 34px;
    height: 34px;
    background: var(--brand-blue);
  }

  .identity {
    position: absolute;
    left: 84px;
    top: 172px;
    white-space: nowrap;
    font-family: "Fira Sans Condensed", sans-serif;
    font-size: 26px;
  }
  .person-name { color: var(--brand-blue); font-weight: 500; }
  .person-title { color: var(--ink-grey); font-weight: 300; margin-left: 12px; }

  .contact {
    position: absolute;
    left: 87px;
    top: 218px;
    margin: 0;
    padding: 0;
    list-style: none;
    font-family: "Fira Sans Condensed", sans-serif;
    font-weight: 300;
    font-size: 23px;
    line-height: 31px;
    color: var(--ink-grey);
  }
  .tagline {
    position: absolute;
    left: 56px;
    top: 344px;
    margin: 0;
    font-family: "Montserrat", sans-serif;
    font-weight: 600;
    font-size: 18px;
    color: var(--tag-grey);
  }

  .manifesto {
    position: absolute;
    right: 103px;
    top: 48px;
    margin: 0;
    text-align: right;
    font-family: "Fira Sans Condensed", sans-serif;
    font-weight: 300;
    font-size: 27px;
    line-height: 31px;
    color: var(--paper);
  }
  .promise {
    position: absolute;
    right: 103px;
    top: 142px;
    margin: 0;
    font-family: "Fira Sans Condensed", sans-serif;
    font-weight: 500;
    font-size: 28px;
    color: var(--paper);
  }
  .website {
    position: absolute;
    right: 65px;
    top: 314px;
    margin: 0;
    font-family: "Fira Sans Condensed", sans-serif;
    font-weight: 300;
    font-size: 23px;
    color: var(--paper);
  }
</style>
</head>
<body>
<main class="canvas">

  <section class="card card-front" aria-label="Card front">
    <div class="side-band" aria-hidden="true"></div>

    <div class="wordmark">
      <span class="wordmark-square"></span>
      <span class="wordmark-name">Hollowmere Advisory</span>
    </div>

    <div class="identity">
      <span class="person-name">Yourfirst Andlastname</span>
      <span class="person-title">- Title of the Individual</span>
    </div>

    <ul class="contact">
      <li>(123) 456-7890 mobile</li>
      <li>(123) 123-4567 office</li>
      <li>person@HollowmereAdvisory.com</li>
    </ul>

    <p class="tagline">Optimize Your Investment in Talent</p>
  </section>

  <section class="card card-back" aria-label="Card back">
    <p class="manifesto">Growth is Imperative. Change is Constant.<br>Talent Executes Strategy.</p>
    <p class="promise">We help you excel at all three.</p>
    <p class="website">www.HollowmereAdvisory.com</p>
  </section>

</main>
</body>
</html>
```